light box menu and wall graphics

HI My name is Derek Vantolla and I am putting together a Pebble Wagons franchise. We are a high quaulity coffee offering and the retail concept is for a in-line store in a busy shopping centre food court. We are a highly visible coffee offering with vibrant bright orange colour (pantone 021 / process m60_y100)
Orange might make a good background on the menu board as it needs to blend in with colour scheme. Also the text has to be at least 15ml and not too busy but clearly legible. The font is: Akzent Rounded
The twin light boxes being used is from http://www.brightframedepot.com.au/pg/lightboxes/new/sdb/light-box-2270K.aspx
They measure in total 3m wide X .6 height

There are two elements to this job, one is the twin menu boards and the other is the wall graphic.
please see wall graphic examples attached.
This graphic is to be painted onto the wall by a sign writter.
The design to go on the wall needs to be a synonymous with our quality coffee vison and match the shop design, I have examples of the type of wall art I am after attached. I was thinking somehow a Cart with wings would look neat and we could incorportate some text into it. Such as "Coffee with Substance makes you feel good" and "Genuine Wagon" Flames could look amazing too!

My website is unfortunately down at the moment but I am attaching plenty

I have just added the menu in easy to read updated format.
Thanks to those who have expressed interest!
Updates

Hi Designers, I have just increased first prize by $100.00

Please note the signage boards run horizontally not vertically.  I have also added more artwork.

thanks

Derek

 HI there, thanks for joining.  I have just updated the brief to make it as clear as possible.

Hope you enjoy this experience.  I am here to answer any questions.

Derek

Thank you for accepting my invitation for this design job.

Look forward to seeing some designs as per brief.

Need to have this finished by Friday the 19th of October.  Thanks

Target Market(s)

Coffee lovers, kids who want hot chocolates, frappes,
etc

Industry/Entity Type

Shopping

Requirements
Must have
• Must have coffee in it for clarity.
Also in the menu any images of food or drink must be photo/posters attached

```html
<!DOCTYPE html>
<html lang="en">
<head>
<meta charset="utf-8">
<title>Light box menu</title>
<link rel="stylesheet" href="https://fonts.googleapis.com/css2?family=Nunito:wght@600;700;800;900&display=swap">
<style>
:root{
  --page:#e9e9e9;
  --cream:#fbf8df;
  --panel:#ffffff;
  --orange:#f08a12;
  --orange-deep:#e06d00;
  --ink:#1f1a17;
  --brown:#4a2a17;
  --bar-edge:#c9c9c9;
}
*{margin:0;padding:0;box-sizing:border-box}
html,body{width:1200px;height:848px;overflow:hidden}
body{background:var(--page);font-family:"Nunito",sans-serif;position:relative}
.menu-board{position:absolute;left:60px;top:284px;width:1050px;height:216px;background:var(--cream);overflow:hidden}
.flame-art{position:absolute;left:0;top:0;width:330px;height:216px}
.menu-panel{position:absolute;left:14px;top:13px;width:1022px;height:193px;border-radius:10px;
  background:linear-gradient(90deg,rgba(255,255,255,.55) 0,rgba(255,255,255,.95) 28%,#fff 60%,rgba(255,255,255,.92));
  box-shadow:0 0 8px rgba(120,100,60,.35)}
.header-bar{position:absolute;left:46px;top:18px;width:991px;height:49px;border-radius:4px;
  background:linear-gradient(#fdfdfd,#e9e9e9);border:1px solid var(--bar-edge);box-shadow:0 2px 4px rgba(0,0,0,.25)}
.abs{position:absolute}
.section-icon{width:44px;height:34px;top:7px}
.section-title{top:4px;font-size:29px;font-weight:900;color:var(--orange);text-shadow:0 0 3px #fff,0 1px 2px rgba(0,0,0,.35)}
.price{top:5px;font-weight:900;color:var(--ink);font-size:21px;line-height:1;white-space:nowrap}
.price .cur{font-size:13px}
.price .amt{color:var(--orange);font-size:21px}
.price .cents{color:var(--orange);font-size:14px}
.price small{display:block;font-size:8px;font-weight:800;color:var(--orange-deep);margin-left:14px;margin-top:1px}
.drink-list{list-style:none;font-weight:900;color:var(--ink);text-shadow:0 0 2px #fff}
.coffee-list{left:87px;top:67px;font-size:16px;line-height:20.5px}
.frappe-list{left:597px;top:67px;font-size:18px;line-height:23px}
.frappe-extra{left:776px;top:67px;font-size:18px;line-height:23px}
.frappe-extra small{font-size:7px;font-weight:700;color:var(--orange);margin-left:2px}
.addons{font-size:8.5px;font-weight:800;color:var(--orange-deep);line-height:10.5px;list-style:none}
.addons li.dot::before{content:"•";color:var(--ink);margin-right:5px}
.addons .lead{color:var(--ink);margin-right:4px}
.addons .muted{color:var(--orange);font-weight:600}
.coffee-addons{left:339px;top:68px}
.coffee-addons .base{font-size:16px;font-weight:900;color:var(--orange);line-height:18px}
.coffee-addons .base span{font-size:9px;color:var(--ink);margin-right:4px}
.frappe-addons{left:768px;top:136px;font-size:9.5px;line-height:12px}
.brand-name{left:930px;top:150px;font-size:15px;font-weight:900;color:var(--brown);display:flex;align-items:center;gap:5px}
.brand-name i{display:block;width:10px;height:10px;border-radius:50%;background:var(--orange)}
</style>
</head>
<body>
<section class="menu-board" aria-label="Light box menu">
  <div class="flame-art" role="img" aria-label="Orange flame swirl artwork"
       style="background:radial-gradient(ellipse at 0% 90%,#f39a1c 0,#f7b444 35%,rgba(251,248,223,0) 75%)"></div>
  <div class="menu-panel"></div>
  <div class="header-bar">
    <div class="abs section-icon" role="img" aria-label="Coffee cup icon" style="left:15px;background:linear-gradient(#7a4a2a,#4a2a17);border-radius:4px 4px 18px 18px"></div>
    <h2 class="abs section-title" style="left:64px">Coffee</h2>
    <div class="abs price" style="left:230px">S <span class="cur">$</span><span class="amt">3</span><span class="cents">.80</span><small>(1 Shot)</small></div>
    <div class="abs price" style="left:303px">M <span class="cur">$</span><span class="amt">4</span><span class="cents">.50</span><small>(2 Shot)</small></div>
    <div class="abs price" style="left:381px">L <span class="cur">$</span><span class="amt">4</span><span class="cents">.90</span><small>(2 Shot)</small></div>
    <div class="abs section-icon" role="img" aria-label="Frappe cup icon" style="left:519px;width:56px;background:linear-gradient(#7a4a2a,#4a2a17);border-radius:50% 50% 40% 40%"></div>
    <h2 class="abs section-title" style="left:588px">Frappes</h2>
    <div class="abs price" style="left:810px">M <span class="cur">$</span><span class="amt">5</span><span class="cents">.00</span></div>
    <div class="abs price" style="left:876px">L <span class="cur">$</span><span class="amt">5</span><span class="cents">.50</span></div>
  </div>

  <ul class="abs drink-list coffee-list">
    <li>Espresso Shot</li><li>Long Black</li><li>Flat White</li><li>Latte</li><li>Cappuccino</li><li>Hot Chocolate</li>
  </ul>
  <ul class="abs addons coffee-addons">
    <li class="base"><span>$</span>2.90</li>
    <li><span class="lead">+</span>50c</li>
    <li class="dot">Soy</li>
    <li class="dot">Mocha</li>
    <li class="dot">Vienna</li>
    <li class="dot">Decaf (fresh)</li>
    <li class="dot">Syrups; <span class="muted">vanilla, caramel, hazelnut</span></li>
    <li class="dot">Cream</li>
    <li class="dot">Coffee shot</li>
    <li class="dot">White chocolate</li>
  </ul>

  <ul class="abs drink-list frappe-list">
    <li>Vanilla</li><li>Hazelnut</li><li>Caramel</li><li>Chocolate</li><li>Coffee</li>
  </ul>
  <ul class="abs drink-list frappe-extra">
    <li>Chai</li>
    <li>Iced Chocolate<small>1 scoop ice cream</small></li>
    <li>Iced Coffee<small>1 scoop ice cream</small></li>
  </ul>
  <ul class="abs addons frappe-addons">
    <li><span class="lead">+</span>50c</li>
    <li class="dot">Mocha</li>
    <li class="dot">Cream</li>
    <li class="dot">Syrups; <span class="muted">vanilla, caramel, hazelnut</span></li>
  </ul>

  <div class="abs brand-name"><i></i>Pebble Wagons</div>
</section>
</body>
</html>
```